Business Cards- The Manor at Brookridge Golf Club

We would like our business cards to look more high-end. We are a wedding venue that has been in business for 60+ years. We like our logo and our colors - primarily green and a touch of gold/beige. The owner wants our business cards to look more special..

Target Market(s)

Brides who have already toured our venue

Industry/Entity Type

Wedding venue - mansion

Contact Information for Business Card

Name, email, physical address, phone number

Colors
00AB8E
00BBA5
67D7C9
C6EFE9
E9F9F6

Requirements
Must have
• I think we would like our cards to be so pretty that people will want to keep them and will remember the venue. The venue is historic (built in 1850) and beautiful.
Nice to have
• Could we put an image of the building on one side and the contact info on the other?
Should not have
• The color black

```html
<!DOCTYPE html>
<html lang="en">
<head>
<meta charset="utf-8">
<title>The Manor at Brookridge Golf Club – Business Cards</title>
<link href="https://fonts.googleapis.com/css2?family=Playfair+Display:ital,wght@0,400;0,700;1,400&display=swap" rel="stylesheet">
<style>
  :root{
    --backdrop:#ababab;
    --card-white:#ffffff;
    --card-deep:#1f3a2a;
    --card-deep-shade:rgba(20,44,30,.8);
    --green:#7a9a4a;
    --gold:#d4c19c;
    --ink:#2a3326;
    --sky:#1f88c4;
    --facade:#e9ecee;
    --hedge:#3f5a2c;
  }
  *{margin:0;padding:0;box-sizing:border-box}
  html,body{width:1200px;height:1000px;overflow:hidden}
  body{background:var(--backdrop);font-family:"Playfair Display",Georgia,serif;position:relative}

  .card{position:absolute;left:294px;width:612px;height:351px;border-radius:24px;
        box-shadow:0 22px 40px rgba(0,0,0,.28),0 6px 14px rgba(0,0,0,.18);overflow:hidden}

  /* Front */
  .card--front{top:88px;background:var(--card-deep)}
  .venue-photo{position:absolute;inset:0;
    background:
      radial-gradient(ellipse at 50% 55%,rgba(20,44,30,0) 50%,var(--card-deep-shade) 100%),
      linear-gradient(180deg,var(--sky) 0%,#5fb1dc 18%,var(--facade) 30%,#d8dcde 55%,#8a9296 70%,var(--hedge) 82%,#2c4420 100%)}
  .card--front .inner-frame{position:absolute;inset:9px;border:1px solid rgba(255,255,255,.85);border-radius:18px}

  /* Back */
  .card--back{top:552px;background:var(--card-white)}
  .card--back .inner-frame{position:absolute;inset:8px;border:2px solid var(--gold);border-radius:20px}

  .brand{position:absolute;top:60px;left:0;right:0;display:flex;justify-content:center;align-items:center;gap:8px}
  .brand__name{color:var(--green);font-size:19px;font-weight:400}
  .brand__mark{width:14px;height:14px;border-radius:50%;background:var(--gold)}

  .person{position:absolute;top:160px;left:0;right:0;text-align:center}
  .person__name{color:var(--green);font-size:24px;font-weight:700;line-height:1.2}
  .person__title{color:var(--green);font-size:18px;font-style:italic;line-height:1.3;opacity:.9}
  .person__rule{width:155px;height:3px;background:var(--gold);margin:8px auto 0}

  .contact{position:absolute;left:0;right:0;color:var(--ink);font-size:17px;display:flex;justify-content:center;gap:12px;align-items:center}
  .contact--top{top:266px}
  .contact--bottom{top:297px}
  .contact__item{display:flex;align-items:center;gap:8px}
  .contact__icon{width:22px;height:22px;border-radius:50%;background:var(--gold);display:flex;align-items:center;justify-content:center}
  .contact__icon svg{width:12px;height:12px;fill:var(--ink)}
  .contact__icon .envelope-flap{fill:none;stroke:var(--gold);stroke-width:2}
</style>
</head>
<body>

<section class="card card--front">
  <div class="venue-photo" role="img" aria-label="Photograph of the white historic manor house with curved columned porch, a wedding gown hanging at the entrance, hedges in front and blue sky above"></div>
  <div class="inner-frame"></div>
</section>

<section class="card card--back">
  <div class="inner-frame"></div>

  <div class="brand">
    <span class="brand__name">The Manor at Brookridge Golf Club</span>
    <span class="brand__mark"></span>
  </div>

  <div class="person">
    <div class="person__name">Laura Whitfield</div>
    <div class="person__title">President -Owner</div>
    <div class="person__rule"></div>
  </div>

  <div class="contact contact--top">
    <span class="contact__item">
      <span class="contact__icon"><svg viewBox="0 0 24 24"><path d="M6.6 10.8a15.1 15.1 0 0 0 6.6 6.6l2.2-2.2a1 1 0 0 1 1-.25 11.4 11.4 0 0 0 3.6.57 1 1 0 0 1 1 1V20a1 1 0 0 1-1 1A17 17 0 0 1 3 4a1 1 0 0 1 1-1h3.5a1 1 0 0 1 1 1c0 1.25.2 2.45.57 3.6a1 1 0 0 1-.25 1z"/></svg></span>
      (410) 555-0148
    </span>
    <span class="contact__item">
      <span class="contact__icon"><svg viewBox="0 0 24 24"><rect x="2" y="5" width="20" height="14" rx="1.5"/><path class="envelope-flap" d="M3 6l9 7 9-7"/></svg></span>
      info@brookridgegolfclub.com
    </span>
  </div>

  <div class="contact contact--bottom">
    <span class="contact__item">
      <span class="contact__icon"><svg viewBox="0 0 24 24"><path d="M12 2a7 7 0 0 0-7 7c0 5.2 7 13 7 13s7-7.8 7-13a7 7 0 0 0-7-7zm0 9.5A2.5 2.5 0 1 1 12 6.5a2.5 2.5 0 0 1 0 5z"/></svg></span>
      2270 Hollins Rd., Brookridge, MD 21208
    </span>
  </div>
</section>

</body>
</html>
```